依頼詳細
おしゃれなイメージを希望しています。

掲載してもらいたい内容を載せています
宜しくお願いします。
①24時間営業
②11/6新規オープン(予定です。後日決定します)
③アクセスマップ(新しくできた『ふわりGATE』というモール内にコインランドリーが開店するということがわかるように)国道217号沿いでハナマルマートがあります。
④店内写真、屋外写真
⑤12/14まで全機種半額
洗濯乾燥8kg 900円→400円
洗濯乾燥15kg 1200円→600円
洗濯乾燥22kg 1500円→700円
洗濯のみ15kg 600円→300円
洗濯のみ22kg 900円→400円
洗濯のみ32kg 1100円→500円
乾燥のみ14kg 100円/10分→100円/20分
乾燥のみ25kg 100円/8分→100円/16分
シューズ用洗濯機 200円→100円
⑤洗濯機から乾燥機に移す面倒な手間いらずの全自動洗濯乾燥機を導入
⑥ふとんクリーニング店プロデュースなので羽毛布団、こたつ布団、毛布の洗濯も安心
⑦天然由来成分とEM(人体にも環境にもやさしい善玉菌の集合体)を配合した洗剤を使用しています。
記載項目
店名ロゴ(添付)、住所(大分市北松原215-3ふわりGATE C-204)、地図、店舗写真、店内写真
サイズ
A5
ページ数
両面
希望イメージ
シンプル 複雑
単色 カラフル
暗い 明るい
日常 高級
遊び心 厳粛
未来的 伝統的
女性的 男性的
希望する色
設定なし
納品ファイル
• イラストレーター形式 (.ai)
補足説明
店舗写真、店内写真は添付写真を当て込んでください。正式な写真は後日差し替えをお願いします。
新規のモール内の店舗ですので地図は大きめに表記をお願いします。
納品はアウトライン化したものとしていないものの両方お願いします。イラストレーターCS2で開けるようにしてください

訴求したい内容が一目でわかりやすい提案だったから

このたびはお忙しい中、多数のご提案をいただきありがとうございました。
今後も依頼していきますので機会がありましたらご提案くださいますようお願いします。
今後ともよろしくお願いします。

```html
<!DOCTYPE html>
<html lang="ja">
<head>
<meta charset="utf-8">
<title>Hanairo Laundry ｜ 11/6 New OPEN</title>
<link rel="stylesheet" href="https://fonts.googleapis.com/css2?family=M+PLUS+Rounded+1c:wght@500;800&family=Zen+Maru+Gothic:wght@500;700;900&family=Shippori+Mincho:wght@600&display=swap">
<style>
  :root {
    --teal: #3ba3a6;
    --teal-dark: #2a7f82;
    --brown: #7a5a3e;
    --brown-dark: #5b402a;
    --plank: #f2f1ee;
    --plank-line: #e2e0db;
    --accent: #f4c43c;
    --orange: #c8703a;
    --ink: #4a3a2c;
    --white: #ffffff;
  }
  * { box-sizing: border-box; margin: 0; padding: 0; }
  html, body { width: 847px; height: 1200px; overflow: hidden; background: var(--white); }
  .flyer {
    position: relative; width: 847px; height: 1200px; overflow: hidden;
    background: repeating-linear-gradient(90deg, var(--plank) 0 120px, var(--plank-line) 120px 122px);
    font-family: "Zen Maru Gothic", sans-serif; color: var(--ink);
  }
  .ribbon { position: absolute; left: 95px; top: 24px; width: 657px; height: 100px; }
  .ribbon-text {
    position: absolute; left: 0; right: 0; top: 40px; text-align: center;
    color: var(--white); font-weight: 700; font-size: 40px; letter-spacing: 4px;
  }
  .title {
    position: absolute; left: 0; right: 0; top: 176px; text-align: center;
    font-family: "M PLUS Rounded 1c", sans-serif; font-weight: 800;
    font-size: 86px; line-height: 1.1; color: var(--brown); letter-spacing: 4px;
    white-space: nowrap;
  }
  .location {
    position: absolute; left: 252px; top: 325px; height: 270px;
    writing-mode: vertical-rl; font-family: "Shippori Mincho", serif;
    font-weight: 600; font-size: 22px; line-height: 34px; letter-spacing: 4px; color: var(--ink);
  }
  .opening {
    position: absolute; left: 316px; top: 332px; width: 216px; height: 216px;
    border-radius: 50%; background: var(--brown); color: var(--white);
    display: flex; flex-direction: column; align-items: center; justify-content: center;
    box-shadow: inset 0 0 0 8px var(--brown), inset 0 0 0 10px rgba(255,255,255,.7);
    font-family: "M PLUS Rounded 1c", sans-serif; line-height: 1;
  }
  .opening-date { font-size: 50px; font-weight: 800; }
  .opening-new { font-size: 24px; font-weight: 500; margin-top: 8px; }
  .opening-word { font-size: 50px; font-weight: 800; margin-top: 2px; }
  .shirt-art {
    position: absolute; left: 545px; top: 340px; width: 215px; height: 230px;
    background: #f7f4ef; border-radius: 40px 40px 16px 16px;
    border: 3px solid #d8cfc3;
  }
  .hours {
    position: absolute; left: 598px; top: 400px; width: 126px; height: 126px;
    border-radius: 50%; border: 3px solid var(--orange); color: var(--orange);
    display: flex; flex-direction: column; align-items: center; justify-content: center;
    font-family: "M PLUS Rounded 1c", sans-serif; font-weight: 800; line-height: 1.05;
  }
  .hours-time { font-size: 40px; }
  .hours-label { font-size: 30px; }
  .interior-photo {
    position: absolute; left: 0; top: 595px; width: 847px; height: 525px;
    background: linear-gradient(180deg, #e9e8e5 0%, #d9d7d3 48%, #8f6e50 62%, #6e5038 100%);
  }
  .staff-art {
    position: absolute; left: 650px; top: 860px; width: 170px; height: 260px;
    background: linear-gradient(180deg, #f1e3cf, #e6c98a); border-radius: 80px 80px 10px 10px;
  }
  .staff-note {
    position: absolute; left: 610px; top: 820px; font-size: 15px; color: var(--brown-dark);
    transform: rotate(-12deg); font-weight: 700; background: rgba(255,255,255,.75);
    padding: 2px 6px; border-radius: 4px;
  }
  .offer {
    position: absolute; left: 170px; top: 870px; width: 468px;
    background: var(--white); border: 3px solid var(--teal);
  }
  .offer-head {
    background: var(--teal); color: var(--white); text-align: center;
    font-weight: 900; font-size: 30px; padding: 8px 0 10px; letter-spacing: 1px;
  }
  .offer-half { color: var(--accent); font-size: 40px; }
  .offer-body { display: flex; align-items: center; gap: 14px; padding: 12px 14px 14px; }
  .offer-tag {
    font-size: 15px; font-weight: 700; color: var(--white); background: var(--orange);
    border-radius: 50%; width: 64px; height: 64px; flex: none;
    display: flex; align-items: center; justify-content: center;
  }
  .offer-item { flex: 1; text-align: center; font-size: 19px; font-weight: 700; line-height: 1.45; }
  .offer-item + .offer-item { border-left: 2px dotted var(--teal); }
  .offer-price { color: var(--orange); font-size: 21px; }
  .brand {
    position: absolute; left: 0; top: 1120px; width: 847px; height: 80px; background: var(--white);
    display: flex; align-items: center; justify-content: center; gap: 14px;
  }
  .brand-mark { width: 22px; height: 22px; background: var(--teal); }
  .brand-name { font-weight: 900; font-size: 36px; color: var(--teal); letter-spacing: 1px; }
</style>
</head>
<body>
<main class="flyer">
  <svg class="ribbon" viewBox="0 0 657 100" aria-hidden="true">
    <polygon points="0,38 60,38 60,100 0,100 22,69" fill="var(--teal-dark)"/>
    <polygon points="657,38 597,38 597,100 657,100 635,69" fill="var(--teal-dark)"/>
    <rect x="40" y="24" width="577" height="64" rx="3" fill="var(--teal)"/>
  </svg>
  <p class="ribbon-text">女性と衣類に優しい</p>

  <h1 class="title">コインランドリー</h1>

  <p class="location">国道２１７号線沿い<br>ふわりGATE内に</p>

  <div class="opening">
    <span class="opening-date">11/6</span>
    <span class="opening-new">New</span>
    <span class="opening-word">OPEN</span>
  </div>

  <div class="shirt-art" role="img" aria-label="白いシャツのイラスト"></div>
  <div class="hours"><span class="hours-time">24h</span><span class="hours-label">営業</span></div>

  <div class="interior-photo" role="img" aria-label="白い洗濯機が並ぶ木目の床の店内写真"></div>
  <div class="staff-art" role="img" aria-label="店内を案内する女性のイラスト"></div>
  <p class="staff-note">とってもおしゃれな店内です!</p>

  <section class="offer">
    <p class="offer-head">12/14まで全機種 <span class="offer-half">半額</span></p>
    <div class="offer-body">
      <span class="offer-tag">たとえば</span>
      <p class="offer-item">洗濯乾燥8kg<br><span class="offer-price">900円→400円</span></p>
      <p class="offer-item">洗濯のみ32kg<br><span class="offer-price">1,100円→500円</span></p>
    </div>
  </section>

  <footer class="brand">
    <span class="brand-mark"></span>
    <span class="brand-name">Hanairo Laundry</span>
  </footer>
</main>
</body>
</html>
```